Solar appointment reminder card

We are looking for a new design for our appointment reminder card since we have changed our logo. The card should have the new logo along with space for the employee to hand write the customers appointment date, time, the employees name and phone number.
I've uploaded what our old basic appointment card looked like and our new logo.

The cards should be in a standard business card size and could be horizontal or vertical.

```html
<!DOCTYPE html>
<html lang="en">
<head>
<meta charset="utf-8">
<title>Solar Appointment Reminder Card</title>
<link rel="stylesheet" href="https://fonts.googleapis.com/css2?family=Source+Sans+3:wght@400;500&display=swap">
<style>
  :root {
    --card-green: #166350;
    --sun-gold: #f8c21a;
    --label-gold: #f6c51c;
    --edge: #7a8a84;
  }
  html, body {
    margin: 0;
    padding: 0;
    width: 1200px;
    height: 686px;
    overflow: hidden;
    background: #ffffff;
  }
  .reminder-card {
    display: block;
    width: 1200px;
    height: 686px;
  }
  .card-face { fill: var(--card-green); stroke: var(--edge); stroke-width: 1; }
  .card-title {
    font-family: "Source Sans 3", sans-serif;
    font-weight: 500;
    font-size: 60px;
    fill: var(--label-gold);
  }
  .field-label {
    font-family: "Source Sans 3", sans-serif;
    font-weight: 400;
    font-size: 56px;
    letter-spacing: 3px;
    fill: var(--label-gold);
  }
  .write-line { stroke: var(--label-gold); stroke-width: 3.5; stroke-linecap: round; }
  .day-label {
    font-family: "Source Sans 3", sans-serif;
    font-weight: 400;
    font-size: 38px;
    fill: var(--label-gold);
  }
  .day-box { fill: none; stroke: var(--label-gold); stroke-width: 2.5; }
  .footer-band { fill: var(--sun-gold); }
  .web-address {
    font-family: "Source Sans 3", sans-serif;
    font-weight: 400;
    font-size: 35px;
    letter-spacing: 2.5px;
    fill: var(--card-green);
  }
</style>
</head>
<body>
<svg class="reminder-card" viewBox="0 0 1200 686" xmlns="http://www.w3.org/2000/svg">
  <rect class="card-face" x="0.5" y="0.5" width="1199" height="685"/>

  <text class="card-title" x="46" y="86">Your Next Appointment</text>

  <text class="field-label" x="56" y="189">Name</text>
  <line class="write-line" x1="55" y1="200" x2="1145" y2="200"/>

  <text class="field-label" x="56" y="275">Date</text>
  <line class="write-line" x1="55" y1="285" x2="560" y2="285"/>
  <text class="field-label" x="599" y="275">Time</text>
  <line class="write-line" x1="599" y1="285" x2="1145" y2="285"/>

  <text class="field-label" x="56" y="361">Phone</text>
  <line class="write-line" x1="55" y1="371" x2="560" y2="371"/>

  <text class="field-label" x="56" y="455">Details</text>
  <line class="write-line" x1="55" y1="470" x2="1145" y2="470"/>

  <g class="weekday-picker">
    <text class="day-label" x="57" y="533">Mon</text>
    <rect class="day-box" x="151" y="502" width="39" height="39" rx="10"/>
    <text class="day-label" x="298" y="533">Tue</text>
    <rect class="day-box" x="394" y="502" width="39" height="39" rx="10"/>
    <text class="day-label" x="543" y="533">Wed</text>
    <rect class="day-box" x="637" y="502" width="39" height="39" rx="10"/>
    <text class="day-label" x="783" y="533">Thu</text>
    <rect class="day-box" x="863" y="502" width="39" height="39" rx="10"/>
    <text class="day-label" x="1038" y="533">Fri</text>
    <rect class="day-box" x="1100" y="502" width="39" height="39" rx="10"/>
  </g>

  <path class="footer-band" d="M0 686 V658 Q0 618 40 618 H1160 Q1200 618 1200 658 V686 Z"/>
  <text class="web-address" x="610" y="664" text-anchor="middle">www.sunridgevisit.com</text>
</svg>
</body>
</html>
```